Wordpress Design Project

i bought a wordpress template, bought my domain and my hosting package. i need someone to pull it all together and design my website and get it up and running.

i have the content, the logos, the look and feel of my design and i will provide these to you. I will need the headings on the theme to change and there will need to be some customization, including the the Social Icons-would need new icons creating similar in look to the existing ones, and then some minor code changes to have a new option appear in the Theme Options panel (ie; Enter your Linkedin username: , rss feed)

i will want one of the pull down tabs to have

I will want the wordpress theme to be SEO optimized. The site is optimized with SEO in mind, but also want the free WordPress plugin called Total Reach Rankpack added and any others that you feel are compelling.

the theme is: http://layoutbazaar.example/item/halvard-responsive-minimal-html5-theme/4827361?WT.ac=category_item&WT.seg_1=category_item&WT.z_author=PeterDunholt

The following design brief gives more information:

- Business Name? Brightfield Union, LLC dba Brightfield Union

- What do you do? Build coalitions for social good

- How many pages do you need designed and code? see template

- What is your industry? social entrepreneurship

- Describe the target audience for your website design? general public

- What 3 things would you like to communicate to your audience through your website design? 1. we are progressive 2. We use the power and merits of Capitalism to transcend poverty, preserve our planet and harness the collective power of the people 3. we are change makers
- How is your company different from your competitors? i invented a business model that will accomplish the above.

- What website design styles do you like? see theme
- What colors do you want to see in your website design? see theme and see my logo/business card.
- What colors do you NOT want to see in your website design? want to stay consistent with current design.
- What adjectives should best describe your website design? modern, artsy, engaging
- What content must be included in the website design? i will provide that later

ill also want you to provide what a process for working with me, including timeline.
Updates

the headers will be 

Home
Who We Are
What We Do
Our Projects
Blog
Latest News
Contact Us

What I am looking for is a mock up of the home page to mimic the halvard wordpress theme.  the first project we will be working on is bringing vertical urban farming/manufactured in buildings - in disadvantaged neighborhoods. 

i have uploaded an executive summary so you know what we do as a company.

I would like to see what images you come up with and how you will incorporate the logo / existing look and feel into the home page.  this will give me a good idea of whom I would like to hire for the job.  this way you are not spending too much time and I can spot what i like immediately.

please also include your capacity to code according to what is required in the halvard theme.  i want to make sure you are not just a graphic designer as I need the backend and some coding capacity.

thanks.

Target Market(s)

general public / corporate america

Industry/Entity Type

Progressive

Requirements
Must have
• even though this is a corporate website, i want the site to be artsy. i like the grey/black and white look and feel of what the template looks like and i want orange as the highlight color.

i will be adding color photos and video to the site. which i do not have yet.

i uploaded the logo and watermark, along with the front and back of my business card so that we remain consistent.

the watermark is used on my stationary and email template.

i will also need the control panel turned over to me when finished so that i may manage going forward.

i would also like to have an ongoing relationship with the web designer as I will be creating other sites as my business takes off.
Should not have

```html
<!DOCTYPE html>
<html lang="en">
<head>
<meta charset="utf-8">
<title>Brightfield Union — Home</title>
<link href="https://fonts.googleapis.com/css2?family=Roboto+Condensed:wght@700&family=Arimo:ital,wght@0,400;0,700;1,400&display=swap" rel="stylesheet">
<style>
  :root {
    --ink: #222222;
    --text: #555555;
    --accent: #e8571e;
    --rule: #cccccc;
    --frame: #e2e2e2;
    --footer-bg: #2b2e31;
    --footer-text: #e6e6e6;
    --footer-muted: #b9b9b9;
    --white: #ffffff;
  }
  * { margin: 0; padding: 0; box-sizing: border-box; }
  html, body { width: 1130px; height: 1200px; overflow: hidden; background: var(--white); }
  body { font-family: "Arimo", Arial, sans-serif; color: var(--text); position: relative; }
  .abs { position: absolute; }

  /* Section heading */
  .section-title { left: 34px; top: 68px; font-family: "Roboto Condensed", sans-serif; font-weight: 700; font-size: 25px; color: var(--ink); letter-spacing: .3px; }
  .section-divider { left: 251px; top: 50px; width: 1px; height: 69px; background: #bdbdbd; }
  .section-tagline { left: 281px; top: 71px; font-style: italic; font-size: 19px; color: var(--accent); }

  /* Article cards */
  .article { top: 184px; width: 311px; }
  .article-media { width: 311px; height: 186px; border: 2px solid var(--frame); padding: 4px; background: var(--white); }
  .article-media div { width: 100%; height: 100%; }
  .article-title { margin-top: 19px; font-family: "Roboto Condensed", sans-serif; font-weight: 700; font-size: 17px; color: var(--ink); }
  .article-subtitle { margin-top: 1px; font-size: 13.5px; color: var(--accent); }
  .article-date { margin-top: 22px; font-size: 14.5px; color: var(--ink); }
  .article-body { margin-top: 5px; font-size: 13.2px; line-height: 20px; }
  .read-more { display: block; margin-top: 26px; font-size: 12.5px; color: var(--accent); text-decoration: none; }
  .read-more span { font-size: 11px; margin-left: 4px; }
  .article-base { position: absolute; left: 0; top: 464px; width: 311px; height: 7px; background: var(--rule); }

  /* Footer */
  .footer-band { left: 0; top: 692px; width: 1130px; height: 8px; background: #d2d2d2; }
  .footer { left: 0; top: 700px; width: 1130px; height: 500px; background: var(--footer-bg); }
  .footer-col { top: 733px; width: 310px; }
  .footer-heading { font-family: "Roboto Condensed", sans-serif; font-weight: 700; font-size: 18.5px; color: var(--white); letter-spacing: .3px; padding-bottom: 8px; border-bottom: 2px solid var(--white); }
  .feed-item { position: absolute; left: 0; width: 310px; }
  .feed-icon { position: absolute; left: 9px; top: 0; }
  .feed-text { position: absolute; left: 60px; width: 250px; font-size: 13.2px; line-height: 20px; color: var(--footer-text); }
  .feed-text em { font-style: normal; color: var(--accent); }
  .more-link { position: absolute; font-size: 13px; color: var(--accent); text-decoration: none; }
  .gallery-thumb { position: absolute; width: 91px; height: 91px; border: 4px solid #f0f0f0; background: linear-gradient(160deg, #6b625a, #3c3530 60%, #241e1b); }

  .footer-rule { left: 43px; top: 1063px; width: 1043px; height: 2px; background: var(--white); }
  .copyright { left: 46px; top: 1093px; font-size: 12px; line-height: 16px; color: var(--footer-muted); }
  .footer-nav { top: 1093px; font-size: 12.2px; color: var(--white); text-decoration: none; }
</style>
</head>
<body>

  <h1 class="abs section-title">LATEST ARTICLES</h1>
  <div class="abs section-divider"></div>
  <p class="abs section-tagline">See what we have done....</p>

  <article class="abs article" style="left:41px">
    <div class="article-media"><div role="img" aria-label="Photo of dice on a financial chart" style="background:linear-gradient(135deg,#c9452f 0%,#e9e4dc 45%,#9aa0a8 75%,#ece9e4 100%)"></div></div>
    <h2 class="article-title">THE US ECONOMIC DILEMMA .......</h2>
    <p class="article-subtitle">Lorel ipsum dolor sit amet</p>
    <p class="article-date">POSTED ON MARCH 7TH, 2012.</p>
    <p class="article-body">Many also have no hope of paying the mortgage, feeding the kids, or buying gas to fuel the car to get to a job interview. They have no reason to believe things are going to change.</p>
    <a class="read-more" href="#">Read More<span>&raquo;</span></a>
    <div class="article-base"></div>
  </article>

  <article class="abs article" style="left:409px">
    <div class="article-media"><div role="img" aria-label="Photo of a woman smelling flowers on a city balcony" style="background:linear-gradient(100deg,#3f6a2c 0%,#6f8f52 40%,#b7a48a 70%,#d8923a 100%)"></div></div>
    <h2 class="article-title">THE ENVIRONMENTAL DILEMMA.......</h2>
    <p class="article-subtitle">Lorel ipsum dolor sit amet</p>
    <p class="article-date">POSTED ON MARCH 7TH, 2012.</p>
    <p class="article-body">Many also have no hope of paying the mortgage, feeding the kids, or buying gas to fuel the car to get to a job interview. They have no reason to believe things are going to change.</p>
    <a class="read-more" href="#">Read More<span>&raquo;</span></a>
    <div class="article-base"></div>
  </article>

  <article class="abs article" style="left:776px">
    <div class="article-media"><div role="img" aria-label="Photo of a protester holding a cardboard sign" style="background:linear-gradient(100deg,#8d2a2a 0%,#4a4a50 35%,#7b6a58 65%,#b89a74 100%)"></div></div>
    <h2 class="article-title">THE WALL STREET DILEMMA .......</h2>
    <p class="article-subtitle">Lorel ipsum dolor sit amet</p>
    <p class="article-date">POSTED ON MARCH 7TH, 2012.</p>
    <p class="article-body">Many also have no hope of paying the mortgage, feeding the kids, or buying gas to fuel the car to get to a job interview. They have no reason to believe things are going to change.</p>
    <a class="read-more" href="#">Read More<span>&raquo;</span></a>
    <div class="article-base"></div>
  </article>

  <div class="abs footer-band"></div>
  <footer class="abs footer"></footer>

  <!-- Latest tweets -->
  <section class="abs footer-col" style="left:43px">
    <h3 class="footer-heading">LATEST TWEETS</h3>
    <div class="feed-item" style="top:56px">
      <svg class="feed-icon" width="32" height="30" viewBox="0 0 32 30"><path d="M4 4h24v16H14l-7 6v-6H4z" fill="none" stroke="#fff" stroke-width="2" stroke-linejoin="round"/></svg>
      <p class="feed-text">@lorel ipsum dolor sit amet nu no vale ncia esta dimari, <em>2 dyas ago</em></p>
    </div>
    <div class="feed-item" style="top:132px">
      <svg class="feed-icon" width="32" height="30" viewBox="0 0 32 30"><path d="M4 4h24v16H14l-7 6v-6H4z" fill="none" stroke="#fff" stroke-width="2" stroke-linejoin="round"/></svg>
      <p class="feed-text">@lorel ipsum dolor sit amet nu no vale ncia esta dimari, <em>2 dyas ago</em></p>
    </div>
    <div class="feed-item" style="top:205px">
      <svg class="feed-icon" width="32" height="30" viewBox="0 0 32 30"><path d="M4 4h24v16H14l-7 6v-6H4z" fill="none" stroke="#fff" stroke-width="2" stroke-linejoin="round"/></svg>
      <p class="feed-text">@lorel ipsum dolor sit amet nu no vale ncia esta dimari, <em>2 dyas ago</em></p>
    </div>
  </section>

  <!-- Latest news -->
  <section class="abs footer-col" style="left:399px">
    <h3 class="footer-heading">LATEST NEWS</h3>
    <div class="feed-item" style="top:56px">
      <svg class="feed-icon" width="32" height="32" viewBox="0 0 32 32"><rect x="5" y="3" width="22" height="26" rx="2" fill="none" stroke="#fff" stroke-width="2"/><path d="M3 8h4M3 14h4M3 20h4M11 10h12M11 15h12M11 20h12" stroke="#fff" stroke-width="2"/></svg>
      <p class="feed-text">lorel ipsum dolor sit amet nu no vale ncia esta dimari.........</p>
    </div>
    <div class="feed-item" style="top:132px">
      <svg class="feed-icon" width="32" height="32" viewBox="0 0 32 32"><rect x="5" y="3" width="22" height="26" rx="2" fill="none" stroke="#fff" stroke-width="2"/><path d="M3 8h4M3 14h4M3 20h4M11 10h12M11 15h12M11 20h12" stroke="#fff" stroke-width="2"/></svg>
      <p class="feed-text">lorel ipsum dolor sit amet nu no vale ncia esta dimari.........</p>
    </div>
    <div class="feed-item" style="top:205px">
      <svg class="feed-icon" width="32" height="32" viewBox="0 0 32 32"><rect x="5" y="3" width="22" height="26" rx="2" fill="none" stroke="#fff" stroke-width="2"/><path d="M3 8h4M3 14h4M3 20h4M11 10h12M11 15h12M11 20h12" stroke="#fff" stroke-width="2"/></svg>
      <p class="feed-text">lorel ipsum dolor sit amet nu no vale ncia esta dimari.........</p>
    </div>
    <a class="more-link" href="#" style="right:6px;top:263px">More News &raquo;</a>
  </section>

  <!-- Photo gallery -->
  <section class="abs footer-col" style="left:771px">
    <h3 class="footer-heading">PHOTO GALLERY</h3>
    <div class="gallery-thumb" role="img" aria-label="Gallery portrait photo" style="left:2px;top:43px"></div>
    <div class="gallery-thumb" role="img" aria-label="Gallery portrait photo" style="left:110px;top:43px"></div>
    <div class="gallery-thumb" role="img" aria-label="Gallery portrait photo" style="left:219px;top:43px"></div>
    <div class="gallery-thumb" role="img" aria-label="Gallery portrait photo" style="left:2px;top:151px"></div>
    <div class="gallery-thumb" role="img" aria-label="Gallery portrait photo" style="left:110px;top:151px"></div>
    <div class="gallery-thumb" role="img" aria-label="Gallery portrait photo" style="left:219px;top:151px"></div>
    <a class="more-link" href="#" style="right:-6px;top:263px">More Photos &raquo;</a>
  </section>

  <div class="abs footer-rule"></div>
  <p class="abs copyright">&copy; 2012, All Rights Reserved, brightfieldunion.example</p>

  <a class="abs footer-nav" href="#" style="left:503px">Home</a>
  <a class="abs footer-nav" href="#" style="left:566px">Who We Are</a>
  <a class="abs footer-nav" href="#" style="left:667px">What We Do</a>
  <a class="abs footer-nav" href="#" style="left:767px">Our Projects</a>
  <a class="abs footer-nav" href="#" style="left:866px">Blog</a>
  <a class="abs footer-nav" href="#" style="left:922px">Latest News</a>
  <a class="abs footer-nav" href="#" style="left:1024px">Contact Us</a>

</body>
</html>
```